Web Design Project

We are looking for a beautiful, clean web page design for our new web service: Quendara. The idea behind quendara is simple. People tell us where they live and what they love, and we point them towards interesting offers, places and events near them - as reviewed by our experts and their friends. It is available on the web and by phone. We have chosen our logo and know the elements we want on each page. Now we just need a whole a great design to pull it all together.
///
QuenDara
locate, explore and discover the best of your city with quendara
Discover your cities hottest offers
places & venues while sharing
the things that mean the most to you.
Join for free today!
//
Note: we have also had some feedback that the name is difficult to read/pronounce, so we might want to change the color of the word be in quendara so that it stands out. suggestions welcome.
Target Market(s)
Young, urban, savvy consumers
We are looking at this site for inspiration
https://trivenko.example/
elements: blog:latest news, top picks // members area // categories: fashion & beauty; food & drink; entertainment & events
Industry/Entity Type
Events
Look and feel

```html
<!DOCTYPE html>
<html lang="en">
<head>
<meta charset="utf-8">
<title>Quendara – locate, explore and discover the best of your city</title>
<link rel="stylesheet" href="https://fonts.googleapis.com/css2?family=Arimo:ital,wght@0,400;0,700;1,400&family=Kalam:wght@400&display=swap">
<style>
  :root {
    --purple: #6a2b8e;
    --purple-button: #8a5ca6;
    --teal: #0b97b0;
    --teal-dark: #0a7f95;
    --teal-text: #1a93a8;
    --teal-button: #4db3c4;
    --green: #2f7a12;
    --ink: #333333;
    --muted: #666666;
    --panel: #f4f4f5;
    --panel-shade: #ebebec;
    --field: #9ea8a5;
    --footer-light: #b7dfe6;
    --skyline: #b9bfbf;
    --white: #ffffff;
  }
  * { box-sizing: border-box; margin: 0; padding: 0; }
  html, body { width: 935px; height: 1200px; overflow: hidden; }
  body {
    position: relative;
    font-family: "Arimo", Arial, sans-serif;
    color: var(--ink);
    background: linear-gradient(180deg, #ffffff 0%, #f6fbfb 20%, #e4f3f2 55%, #e9f5f5 69%);
  }
  .abs { position: absolute; }

  /* header */
  .brand { left: 30px; top: 92px; display: flex; align-items: center; gap: 10px; }
  .brand-mark { width: 22px; height: 22px; background: var(--teal); }
  .brand-name { font-size: 40px; color: #444; font-weight: 400; letter-spacing: 0.5px; }
  .tagline { left: 263px; top: 57px; color: var(--purple); }
  .tagline .line-1 { font-size: 17px; }
  .tagline .line-2 { font-size: 22px; margin-top: 7px; }
  .quick-links { left: 710px; top: 58px; display: flex; gap: 28px; }
  .quick-links span { width: 30px; height: 30px; border-radius: 4px; background: #eef0f0; display: flex; align-items: center; justify-content: center; }

  /* skyline */
  .skyline { left: 0; top: 755px; width: 935px; height: 75px; background: linear-gradient(180deg, rgba(185,191,191,0.4), var(--skyline)); }

  /* left column */
  .side-heading { font-size: 19px; color: var(--green); }
  .login-title { left: 30px; top: 264px; }
  .field { left: 33px; width: 155px; height: 27px; border-radius: 3px; background: var(--field); color: #f1f1f1; font-size: 10px; font-style: italic; padding: 8px 10px; }
  .field-user { top: 300px; }
  .field-pass { top: 339px; font-size: 13px; font-style: normal; padding-top: 5px; letter-spacing: 2px; }
  .btn { display: flex; align-items: center; justify-content: center; color: var(--white); font-size: 12px; border-radius: 3px; }
  .btn-login { left: 127px; top: 376px; width: 61px; height: 23px; background: var(--teal); font-size: 13px; }
  .categories-title { left: 30px; top: 447px; }
  .category-list { left: 33px; top: 486px; list-style: none; }
  .category-list li { display: flex; align-items: center; gap: 12px; font-size: 13px; color: #444; height: 35.5px; }

  /* main panel */
  .panel { left: 229px; top: 178px; width: 673px; height: 809px; background: var(--panel); border-radius: 8px; box-shadow: 0 0 6px rgba(0,0,0,0.22); overflow: hidden; }
  .panel-news-band { left: 0; top: 652px; width: 673px; height: 157px; background: var(--panel-shade); }
  .slide { left: 246px; top: 193px; width: 644px; height: 220px; border-radius: 9px; border: 2px solid #d9d9d9;
    background: linear-gradient(180deg, #cfd2d4 0%, #c7bfb2 45%, #8f8a84 75%, #5e5a58 100%); overflow: hidden; }
  .slide-ribbon { left: 248px; top: 320px; width: 140px; height: 92px; }
  .slide-ribbon-text { left: 240px; top: 360px; font-family: "Kalam", cursive; color: var(--purple); font-size: 16px; line-height: 17px; transform: rotate(45deg); text-align: center; width: 100px; }
  .arrow { width: 44px; height: 44px; top: 282px; }
  .arrow-prev { left: 219px; }
  .arrow-next { left: 875px; }
  .slide-caption { left: 258px; top: 423px; width: 450px; color: var(--teal-text); font-size: 13px; line-height: 17px; }
  .btn-slide { left: 721px; top: 425px; width: 69px; height: 26px; background: var(--teal-button); }

  .section-title { font-size: 21px; color: var(--purple); }
  .blogs-title { left: 242px; top: 478px; }
  .blogs-text { left: 260px; top: 515px; width: 625px; font-size: 12px; line-height: 19px; color: var(--ink); }
  .btn-blogs { left: 813px; top: 579px; width: 70px; height: 26px; background: var(--purple-button); }
  .picks-title { left: 242px; top: 619px; }
  .pick { width: 134px; height: 144px; background: var(--white); border: 1px solid #c9c9c9; box-shadow: 1px 2px 4px rgba(0,0,0,0.2); padding: 9px 9px 0; }
  .pick-photo { width: 114px; height: 112px; border: 1px solid #999; }
  .pick-caption { font-family: "Kalam", cursive; font-size: 10px; color: #555; text-align: center; margin-top: 3px; }
  .pick-1 { left: 263px; top: 664px; transform: rotate(2deg); }
  .pick-1 .pick-photo { background: linear-gradient(180deg, #7f95b5 0%, #a7b3c2 45%, #3b3f47 70%, #44505e 100%); }
  .pick-2 { left: 423px; top: 664px; transform: rotate(-2deg); }
  .pick-2 .pick-photo { background: linear-gradient(160deg, #5d7462, #34483d 60%, #2b3a36); }
  .pick-3 { left: 583px; top: 664px; transform: rotate(2deg); }
  .pick-3 .pick-photo { background: linear-gradient(180deg, #8fb1d8 0%, #b8cde2 35%, #6f7b55 55%, #5f8a37 100%); }
  .pick-4 { left: 743px; top: 664px; transform: rotate(-2deg); }
  .pick-4 .pick-photo { background: linear-gradient(180deg, #b68b6a 0%, #8a6a55 45%, #5f7768 70%, #4f5f55 100%); }

  /* teal band */
  .teal-band { left: 0; top: 830px; width: 935px; height: 302px; background: var(--teal); }
  .news-title { left: 244px; top: 845px; }
  .news-item { top: 884px; width: 258px; padding-left: 18px; font-size: 12px; line-height: 17px; color: var(--muted); }
  .news-item::before { content: ""; position: absolute; left: 2px; top: 4px; border-left: 5px solid #444; border-top: 4px solid transparent; border-bottom: 4px solid transparent; }
  .news-item-1 { left: 245px; }
  .news-item-2 { left: 582px; }
  .news-more { top: 936px; font-size: 12px; color: var(--purple); text-decoration: underline; }
  .news-more-1 { left: 450px; }
  .news-more-2 { left: 787px; }

  .newsletter-title { left: 30px; top: 860px; font-size: 17px; color: var(--white); }
  .field-mail { left: 30px; top: 895px; width: 175px; height: 28px; background: var(--white); border-radius: 3px; border: 1px solid #cde; color: #777; font-size: 11px; font-style: italic; padding: 7px 8px; }
  .btn-submit { left: 152px; top: 933px; width: 53px; height: 25px; background: linear-gradient(180deg, #ffffff, #cfe9ee); color: #234; box-shadow: 0 1px 2px rgba(0,0,0,0.3); }

  .footer-column { top: 1017px; color: var(--white); }
  .footer-column h3 { font-size: 13px; font-weight: 400; margin-bottom: 6px; }
  .footer-column ul { list-style: none; }
  .footer-column li { font-size: 11px; line-height: 18.7px; padding-left: 14px; position: relative; }
  .footer-column li::before { content: ""; position: absolute; left: 2px; top: 7px; width: 4px; height: 4px; border-radius: 50%; background: var(--white); }

  .bottom-bar { left: 0; top: 1132px; width: 935px; height: 68px; background: var(--footer-light); }
  .copyright { left: 35px; top: 1155px; font-size: 11px; color: #111; }
  .connect { left: 636px; top: 1155px; font-size: 11px; color: #111; }
  .social { top: 1150px; width: 22px; height: 22px; border-radius: 3px; }
</style>
</head>
<body>

<header>
  <div class="abs brand"><span class="brand-mark"></span><span class="brand-name">quendara</span></div>
  <div class="abs tagline">
    <p class="line-1">locate, explore and discover the best of your city</p>
    <p class="line-2">with quendara.....</p>
  </div>
  <nav class="abs quick-links" aria-label="Quick links">
    <span title="Home"><svg width="22" height="20" viewBox="0 0 22 20"><path d="M11 2 L21 11 H18 V19 H13 V14 H9 V19 H4 V11 H1 Z" fill="#555"/></svg></span>
    <span title="Account"><svg width="22" height="22" viewBox="0 0 22 22"><circle cx="11" cy="6" r="5" fill="#555"/><path d="M1 21 C1 13 21 13 21 21 Z" fill="#555"/></svg></span>
    <span title="Contact"><svg width="24" height="20" viewBox="0 0 24 20"><path d="M2 7 C2 1 22 1 22 7 L18 8 L17 5 H7 L6 8 Z" fill="#555"/><rect x="5" y="9" width="14" height="10" rx="2" fill="#555"/><circle cx="12" cy="14" r="3" fill="#eef0f0"/></svg></span>
  </nav>
</header>

<div class="abs skyline" role="img" aria-label="Grey city skyline silhouette with speech bubbles"></div>

<aside>
  <h2 class="abs side-heading login-title">Log in</h2>
  <div class="abs field field-user">user name</div>
  <div class="abs field field-pass">●●●●●●</div>
  <div class="abs btn btn-login">Log in</div>
  <h2 class="abs side-heading categories-title">categories</h2>
  <ul class="abs category-list">
    <li><svg width="10" height="8" viewBox="0 0 10 8"><path d="M0 0 L5 4 L0 8 Z M4 0 L9 4 L4 8 Z" fill="#666"/></svg>Fashion &amp; Beauty</li>
    <li><svg width="10" height="8" viewBox="0 0 10 8"><path d="M0 0 L5 4 L0 8 Z M4 0 L9 4 L4 8 Z" fill="#666"/></svg>Food &amp; Drink</li>
    <li><svg width="10" height="8" viewBox="0 0 10 8"><path d="M0 0 L5 4 L0 8 Z M4 0 L9 4 L4 8 Z" fill="#666"/></svg>Entertainment &amp; Events</li>
  </ul>
</aside>

<div class="abs teal-band"></div>

<main class="abs panel">
  <div class="abs panel-news-band"></div>
</main>

<div class="abs slide" role="img" aria-label="City square with domed churches, an obelisk and crowds of people"></div>
<svg class="abs slide-ribbon" viewBox="0 0 140 92" aria-hidden="true"><path d="M0 0 L140 92 H8 Q0 92 0 84 Z" fill="#ffffff"/></svg>
<p class="abs slide-ribbon-text">Join for<br>Free Today!</p>
<svg class="abs arrow arrow-prev" viewBox="0 0 44 44" aria-label="Previous"><circle cx="22" cy="22" r="21" fill="#0b97b0" stroke="#fff" stroke-width="2"/><path d="M26 13 L16 22 L26 31 Z" fill="#fff"/></svg>
<svg class="abs arrow arrow-next" viewBox="0 0 44 44" aria-label="Next"><circle cx="22" cy="22" r="21" fill="#0b97b0" stroke="#fff" stroke-width="2"/><path d="M18 13 L28 22 L18 31 Z" fill="#fff"/></svg>
<p class="abs slide-caption">Discover your cities hottest offers places &amp; venues while sharing the things that mean the most to you.</p>
<div class="abs btn btn-slide">View more</div>

<h2 class="abs section-title blogs-title">Our Blogs</h2>
<p class="abs blogs-text">Many desktop publishing packages and web page editors now use Lorem Ipsum as their default model text, and a search for 'lorem ipsum' will uncover many web sites still in their infancy. Various versions have evolved over the years, sometimes by accident, sometimes on purpose (injected humour and the like).</p>
<div class="abs btn btn-blogs">View more</div>

<h2 class="abs section-title picks-title">Top picks of this Week</h2>
<figure class="abs pick pick-1"><div class="pick-photo" role="img" aria-label="Gothic tower by a river under a cloudy sky"></div><figcaption class="pick-caption">Lorem ipsum</figcaption></figure>
<figure class="abs pick pick-2"><div class="pick-photo" role="img" aria-label="Rafting boat on dark green water"></div><figcaption class="pick-caption">Lorem ipsum</figcaption></figure>
<figure class="abs pick pick-3"><div class="pick-photo" role="img" aria-label="Green grassy hill with rocky ruins"></div><figcaption class="pick-caption">Lorem ipsum</figcaption></figure>
<figure class="abs pick pick-4"><div class="pick-photo" role="img" aria-label="Canal lined with moored gondolas and old buildings"></div><figcaption class="pick-caption">Lorem ipsum</figcaption></figure>

<h2 class="abs section-title news-title">Latest News</h2>
<p class="abs news-item news-item-1">Talvenor are also reproduced in their exact original form, accompanied by English versions from the 1914 translation.</p>
<p class="abs news-item news-item-2">Talvenor are also reproduced in their exact original form, accompanied by English versions from the 1914 translation.</p>
<a class="abs news-more news-more-1">View more</a>
<a class="abs news-more news-more-2">View more</a>

<section>
  <h2 class="abs newsletter-title">News Letter</h2>
  <div class="abs field-mail">Enter mail ID</div>
  <div class="abs btn btn-submit">Submit</div>
</section>

<footer>
  <div class="abs footer-column" style="left:68px"><h3>Menu</h3><ul><li>Home</li><li>About US</li><li>Contact Us</li><li>Site map</li></ul></div>
  <div class="abs footer-column" style="left:219px"><h3>Lorem Ipusem</h3><ul><li>dolor sit</li><li>tempor nisl</li><li>congue ligula</li><li>Aenean at</li></ul></div>
  <div class="abs footer-column" style="left:406px"><h3>Lorem Ipusem</h3><ul><li>consectetur</li><li>porttitor tempor</li><li>Nunc ultrices</li><li>Quam eleifend</li></ul></div>
  <div class="abs footer-column" style="left:600px"><h3>Lorem Ipusem</h3><ul><li>Aliquam sit</li><li>magna et</li><li>mattis adipiscing</li><li>amet non</li></ul></div>
  <div class="abs footer-column" style="left:810px"><h3>Lorem Ipusem</h3><ul><li>Nulla vehicul</li><li>purus ut</li><li>Ornare feugiat</li><li>Imperdiet massa</li></ul></div>

  <div class="abs bottom-bar"></div>
  <p class="abs copyright">Copyright © 2011 www.quendara.com &nbsp; All rights reserved</p>
  <p class="abs connect">Connect with us :</p>
  <span class="abs social" style="left:732px;background:#3b5a98"></span>
  <span class="abs social" style="left:769px;background:#45b0e3"></span>
  <span class="abs social" style="left:807px;background:#f06a1d"></span>
  <span class="abs social" style="left:845px;background:#1b6fa6"></span>
  <span class="abs social" style="left:882px;background:#4a9a3c"></span>
</footer>

</body>
</html>
```